Pest Control Company needs business card!

Hi there, we need a business card designed for our new Pest Control Company. Ideally this card will be simple, yet feel elegant and high end. We want to use the colours Orange, Black and White. Please see our attached logo for the exact colours.

Business card details:

Phone - 0461 275 804
Name - Gavin Holloway
Email - Info@steadfastverminguard.com.au

We would also like to include the following list with dot points:

SERVICES / INSPECTIONS

Termites, Wood Borers, Ants, Cockroaches, Spiders, Fleas, Mice, Rats, Bed Bugs, & More!

```html
<!DOCTYPE html>
<html lang="en">
<head>
<meta charset="utf-8">
<title>Steadfast Vermin Guard – Business Card</title>
<link href="https://fonts.googleapis.com/css2?family=Montserrat:wght@400;600;800&family=Roboto+Condensed:wght@400;500&display=swap" rel="stylesheet">
<style>
  :root {
    --page: #f2f2f2;
    --card: #000000;
    --orange: #f47f20;
    --white: #ffffff;
    --rule: #e6e6e6;
  }
  html, body { margin: 0; padding: 0; }
  body {
    width: 853px; height: 1200px; overflow: hidden;
    background: var(--page);
    position: relative;
  }
  .card {
    position: absolute; left: 46px; top: 382px;
    width: 760px; height: 436px;
    background: var(--card);
    box-shadow: 10px 12px 18px rgba(0,0,0,0.25);
    overflow: hidden;
  }
  .holder-name {
    position: absolute; left: 45px; top: 44px; margin: 0;
    font-family: "Montserrat", sans-serif; font-weight: 400;
    font-size: 37px; letter-spacing: 2px; color: var(--white); line-height: 1;
  }
  .holder-name strong { font-weight: 600; }
  .rule {
    position: absolute; height: 1.5px; background: var(--rule);
  }
  .rule::before {
    content: ""; position: absolute; left: 0; top: -2px;
    width: 23px; height: 5px; background: var(--orange);
  }
  .rule--name { left: 45px; top: 94px; width: 296px; }
  .rule--services { left: 96px; top: 358px; width: 557px; }
  .contact-bar {
    position: absolute; left: 0; top: 182px; width: 33px; height: 81px;
    background: var(--orange);
  }
  .contact-list {
    position: absolute; left: 45px; top: 178px; margin: 0; padding: 0; list-style: none;
    font-family: "Montserrat", sans-serif; color: var(--orange);
  }
  .contact-list li { display: flex; align-items: center; height: 29px; }
  .contact-list li.phone { height: 34px; font-size: 24px; letter-spacing: 1px; }
  .contact-list li.email, .contact-list li.web { font-size: 18.5px; }
  .contact-list svg { width: 22px; height: 22px; margin-right: 12px; flex: none; }
  .brand {
    position: absolute; left: 452px; top: 60px;
    display: flex; align-items: center; gap: 14px;
  }
  .brand-name {
    font-family: "Montserrat", sans-serif; font-weight: 800;
    font-size: 27px; line-height: 1.05; color: var(--orange);
    letter-spacing: -0.5px; text-transform: uppercase;
  }
  .brand-dot { width: 62px; height: 62px; border-radius: 50%; background: var(--orange); flex: none; }
  .services-title {
    position: absolute; left: 0; right: 0; top: 320px; margin: 0; text-align: center;
    font-family: "Roboto Condensed", sans-serif; font-weight: 500;
    font-size: 23px; letter-spacing: 1.2px; color: var(--white); line-height: 1;
  }
  .services-list {
    position: absolute; left: 0; right: 0; top: 367px; margin: 0; text-align: center;
    font-family: "Roboto Condensed", sans-serif; font-weight: 400;
    font-size: 20.5px; line-height: 31px; color: var(--orange);
  }
</style>
</head>
<body>
  <section class="card" aria-label="Business card">
    <h1 class="holder-name"><strong>Gavin</strong> Holloway</h1>
    <div class="rule rule--name"></div>

    <div class="brand">
      <div class="brand-name">Steadfast<br>Vermin<br>Guard</div>
      <div class="brand-dot"></div>
    </div>

    <div class="contact-bar"></div>
    <ul class="contact-list">
      <li class="phone">
        <svg viewBox="0 0 24 24" aria-hidden="true"><path fill="#fff" d="M6.6 2.5c.6-.3 1.3-.1 1.6.5l2 3.6c.3.6.2 1.2-.3 1.6L8.4 9.4c1.1 2.5 3.6 5 6.2 6.2l1.2-1.5c.4-.5 1.1-.6 1.6-.3l3.6 2c.6.3.8 1 .5 1.6l-1.2 2.4c-.4.8-1.3 1.3-2.2 1.1C10.5 19.7 4.3 13.5 3.1 5.9 3 5 3.4 4.1 4.2 3.7z"/></svg>
        0461 275 804
      </li>
      <li class="email">
        <svg viewBox="0 0 24 24" aria-hidden="true"><rect x="2" y="5" width="20" height="14" fill="#fff"/><path d="M2 5l10 8 10-8" fill="none" stroke="#000" stroke-width="1.8"/></svg>
        Info@steadfastverminguard.com.au
      </li>
      <li class="web">
        <svg viewBox="0 0 24 24" aria-hidden="true"><g fill="none" stroke="#fff" stroke-width="1.8"><circle cx="11" cy="11" r="8.5"/><ellipse cx="11" cy="11" rx="3.6" ry="8.5"/><path d="M2.5 11h17M4 6.5h14M4 15.5h9"/></g><path d="M14 13l7 4-3 1 2 3-1.5 1-2-3-2 2z" fill="#fff" stroke="#000" stroke-width=".8"/></svg>
        steadfastverminguard.com.au
      </li>
    </ul>

    <h2 class="services-title">SERVICES / INSPECTIONS</h2>
    <div class="rule rule--services"></div>
    <p class="services-list">
      • Termites • Wood Borers • Ants • Cockroaches• Spiders • Fleas<br>
      • Mice• Rats • Bed Bugs &amp; More!
    </p>
  </section>
</body>
</html>
```